Tarvil GmbH business card

We Tarvil GmbH based in Switzerland are looking for a business card design. The Fresh Jung, appealing to customers of all kinds. We already have a logo to upload but still a business card. Details: Tarvil GmbH Address: Lindenweg 14b in 9412 Rudolfen. Tel: 41 76 392 00 47, web: Tarvil.ch, E-mail: info@Tarvil.ch Facebook: Tarvil GmbH. I am the Managing Director: Lukas Verholt. On reverse: Title: Transporter and bus rental Gross: Without deposit Super prices
Contact Information for Business Card
Siehe Projektbeschreibung
Requirements
Should not have
- Other pictures

```html
<!DOCTYPE html>
<html lang="de">
<head>
<meta charset="utf-8">
<title>Tarvil GmbH – Visitenkarte</title>
<link rel="stylesheet" href="https://fonts.googleapis.com/css2?family=Lato:wght@400;700;900&display=swap">
<style>
  :root {
    --navy: #27266b;
    --navy-soft: #3a3a82;
    --steel: #8aa0bd;
    --ink: #2b2a6e;
    --muted: #8a95a8;
    --paper: #ffffff;
    --stage: #2a2a2c;
  }
  * { box-sizing: border-box; margin: 0; padding: 0; }
  html, body { width: 1200px; height: 852px; overflow: hidden; }
  body {
    background: var(--stage);
    font-family: "Lato", Arial, sans-serif;
    position: relative;
  }
  .card {
    position: absolute;
    width: 540px;
    height: 310px;
    border-radius: 22px;
    overflow: hidden;
  }
  .card--front { left: 70px; top: 80px; background: var(--navy); }
  .card--back { left: 590px; top: 462px; background: var(--paper); }

  .brand { display: flex; align-items: center; gap: 12px; }
  .brand__mark { width: 30px; height: 30px; }
  .brand__name { font-weight: 900; letter-spacing: 1px; line-height: 1; }
  .brand__suffix { font-weight: 900; font-size: 13px; letter-spacing: 2px; align-self: flex-start; margin-top: 2px; }

  .card--front .brand { position: absolute; left: 130px; top: 128px; color: var(--paper); }
  .card--front .brand__mark { background: var(--paper); }
  .card--front .brand__name { font-size: 48px; }
  .card--front .brand__suffix { color: var(--paper); }
  .front__glow {
    position: absolute; right: -60px; top: -80px;
    width: 320px; height: 320px; border-radius: 50%;
    background: var(--navy-soft); opacity: .35;
  }

  .card--back .brand { position: absolute; left: 40px; top: 140px; color: var(--navy); }
  .card--back .brand__mark { background: var(--navy); width: 24px; height: 24px; }
  .card--back .brand__name { font-size: 34px; }
  .card--back .brand__suffix { font-size: 10px; }

  .divider { position: absolute; left: 290px; top: 58px; width: 1px; height: 130px; background: var(--muted); }

  .contact { position: absolute; left: 310px; top: 58px; color: var(--ink); }
  .contact__name { font-weight: 700; font-size: 18px; }
  .contact__role { font-size: 13px; color: var(--muted); margin-bottom: 10px; }
  .contact__list { list-style: none; font-size: 13px; }
  .contact__list li { display: flex; align-items: center; gap: 8px; height: 19px; }
  .icon { width: 13px; height: 13px; flex: none; }

  .address { position: absolute; right: 34px; bottom: 34px; font-size: 13px; font-weight: 700; color: var(--ink); }
  .band { position: absolute; left: 0; right: 0; bottom: 0; height: 14px; display: flex; }
  .band__navy { width: 58%; background: var(--navy); }
  .band__steel { flex: 1; background: var(--steel); }
</style>
</head>
<body>
  <section class="card card--front" aria-label="Vorderseite">
    <div class="front__glow"></div>
    <div class="brand">
      <span class="brand__mark"></span>
      <span class="brand__name">TARVIL</span>
      <span class="brand__suffix">GMBH</span>
    </div>
  </section>

  <section class="card card--back" aria-label="Rückseite">
    <div class="brand">
      <span class="brand__mark"></span>
      <span class="brand__name">TARVIL</span>
      <span class="brand__suffix">GMBH</span>
    </div>
    <div class="divider"></div>
    <div class="contact">
      <p class="contact__name">Lukas Verholt</p>
      <p class="contact__role">Manager</p>
      <ul class="contact__list">
        <li>
          <svg class="icon" viewBox="0 0 13 13"><rect width="13" height="13" rx="2" fill="var(--ink)"/><path d="M3.5 3h2l.8 2-1.2.8a5 5 0 0 0 2.1 2.1l.8-1.2 2 .8v2c-3.8.3-6.8-2.7-6.5-6.5z" fill="#fff"/></svg>
          +41 76 392 00 47
        </li>
        <li>
          <svg class="icon" viewBox="0 0 13 13"><rect width="13" height="13" rx="2" fill="var(--ink)"/><rect x="3" y="3.5" width="7" height="6" rx="1" fill="none" stroke="#fff"/></svg>
          www.Tarvil.ch
        </li>
        <li>
          <svg class="icon" viewBox="0 0 13 13"><rect width="13" height="13" rx="2" fill="var(--ink)"/><rect x="3" y="4" width="7" height="5" fill="none" stroke="#fff"/><path d="M3 4l3.5 3L10 4" fill="none" stroke="#fff"/></svg>
          info@Tarvil.ch
        </li>
        <li>
          <svg class="icon" viewBox="0 0 13 13"><rect width="13" height="13" rx="2" fill="var(--ink)"/></svg>
          Tarvil GmbH
        </li>
      </ul>
    </div>
    <p class="address">Lindenweg 14b in 9412 Rudolfen</p>
    <div class="band"><span class="band__navy"></span><span class="band__steel"></span></div>
  </section>
</body>
</html>
```